Photographer website

This website will contain information to sell the services of marvello tebani an up and coming photographer based in london

Target Market(s)

SME's for corporate head shots
mums for kids parties
actors - for headshots
up and coming models

Industry/Entity Type

Photographer

Number of Pages Required

3 page

Requirements
Must have
• Home
• About me
• Contact me
• Portfolio or gallery

```html
<!DOCTYPE html>
<html lang="en">
<head>
<meta charset="utf-8">
<title>Marvello Tebani – Photographer</title>
<link href="https://fonts.googleapis.com/css2?family=Lato:wght@300;400;700&family=Open+Sans:wght@400&family=Playfair+Display:ital@1&display=swap" rel="stylesheet">
<style>
  :root {
    --white: #ffffff;
    --ink: #4a4a4a;
    --icon-grey: #666666;
    --accent-taupe: #9a8b72;
    --link-blue: #3f6f93;
    --tooltip-bg: #0a0a0a;
    --sky: #3f86c4;
    --building: #8a8478;
    --shadow: #1d1f24;
  }
  * { box-sizing: border-box; margin: 0; padding: 0; }
  html, body { width: 1200px; height: 729px; overflow: hidden; background: var(--white); }
  body { position: relative; font-family: "Lato", sans-serif; }

  .hero { position: absolute; left: 0; top: 0; width: 1200px; height: 437px; overflow: hidden; }
  .hero-photo {
    position: absolute; inset: 0;
    background:
      radial-gradient(ellipse 260px 300px at 560px 250px, rgba(40,35,35,.55), transparent 70%),
      linear-gradient(90deg, rgba(0,0,0,0) 70%, rgba(20,20,24,.75) 100%),
      linear-gradient(180deg, var(--sky) 0%, #7fa9cf 18%, var(--building) 34%, #6c675f 60%, #4b3b3a 85%, var(--shadow) 100%);
  }
  .hero-title {
    position: absolute; left: 0; right: 0; top: 112px; text-align: center;
    color: var(--white); font-weight: 300; font-size: 48px; letter-spacing: 3px;
    text-transform: uppercase; padding-left: 40px;
  }
  .hero-tagline {
    position: absolute; left: 0; right: 0; top: 181px; text-align: center;
    color: var(--white); font-family: "Playfair Display", serif; font-style: italic; font-size: 17px;
    padding-left: 40px;
  }
  .main-nav {
    position: absolute; left: 280px; top: 314px; width: 639px; height: 42px;
    border-top: 2px solid var(--white); border-bottom: 1px solid var(--white);
    display: flex; align-items: center; padding-left: 10px;
  }
  .main-nav a {
    color: var(--white); text-decoration: none; font-weight: 700; font-size: 13px;
    text-transform: uppercase; margin-right: 19px; white-space: nowrap;
  }
  .main-nav a.is-current { text-decoration: underline; }
  .main-nav a.wide { margin-right: 56px; }

  .tooltip {
    position: absolute; left: 862px; top: 0; width: 231px; height: 50px;
    background: var(--tooltip-bg); color: var(--white); border-radius: 0 0 3px 3px;
    font-family: "Open Sans", sans-serif; font-size: 14px; line-height: 20px;
    text-align: center; padding-top: 6px;
  }

  .section-heading {
    position: absolute; left: 164px; top: 486px;
    color: var(--accent-taupe); font-weight: 700; font-size: 16px; text-transform: uppercase;
  }
  .section-rule { position: absolute; left: 164px; top: 516px; width: 57px; height: 3px; background: var(--accent-taupe); }

  .video-icon { position: absolute; left: 174px; top: 569px; width: 236px; height: 180px; }

  .cta {
    position: absolute; left: 460px; top: 557px;
    color: var(--ink); font-weight: 700; font-size: 24px;
  }
  .cta a { color: var(--link-blue); text-decoration: underline; }
</style>
</head>
<body>
  <header class="hero">
    <div class="hero-photo" role="img" aria-label="Photographer holding a camera to his eye at an outdoor street market"></div>
    <h1 class="hero-title">Marvello Tebani</h1>
    <p class="hero-tagline">up and coming photographer based in london</p>
    <nav class="main-nav">
      <a class="is-current" href="#about">About Marvello Tebani</a>
      <a class="wide" href="#">Button</a>
      <a href="#">Portfolio</a>
      <a href="#">Contact Me</a>
      <a href="#">Find me on Snapcircle</a>
    </nav>
  </header>

  <div class="tooltip">Don't forget to check out the mobile views!</div>

  <section id="about">
    <h2 class="section-heading">About Marvello Tebani</h2>
    <div class="section-rule"></div>
    <svg class="video-icon" viewBox="0 0 236 180" fill="none" stroke="var(--icon-grey)" stroke-width="6" stroke-linecap="round" aria-hidden="true">
      <rect x="4" y="4" width="228" height="200" rx="8"/>
      <line x1="48" y1="4" x2="48" y2="204"/>
      <line x1="188" y1="4" x2="188" y2="204"/>
      <g stroke-width="7">
        <line x1="20" y1="29" x2="32" y2="29"/><line x1="20" y1="54" x2="32" y2="54"/>
        <line x1="20" y1="79" x2="32" y2="79"/><line x1="20" y1="104" x2="32" y2="104"/>
        <line x1="20" y1="129" x2="32" y2="129"/><line x1="20" y1="154" x2="32" y2="154"/>
        <line x1="204" y1="29" x2="216" y2="29"/><line x1="204" y1="54" x2="216" y2="54"/>
        <line x1="204" y1="79" x2="216" y2="79"/><line x1="204" y1="104" x2="216" y2="104"/>
        <line x1="204" y1="129" x2="216" y2="129"/><line x1="204" y1="154" x2="216" y2="154"/>
      </g>
      <path d="M90 65 L145 103 L90 141 Z" stroke-linejoin="round"/>
    </svg>
    <p class="cta">***CLICK<a href="#"> HERE</a></p>
  </section>
</body>
</html>
```